Business card Zottelgarten

Business card is for a self-employed dog trainer with own dog school. Name and logo of the dog school are available. Color specifications as well. The design should be classy and minimalist, but also modern. An already existing idea would be: Front: Only the logo Back: Contact data

Font styles to use
Serif
Sans Serif
Other font styles liked:
• Trajan Pro

Colors
f78f20

Requirements
Must have
• Name: Margit Wendler-Rasch Title: Dipl. Dog Trainer Contain my logo Follow my font and color preferences (see files)

```html
<!DOCTYPE html>
<html lang="de">
<head>
<meta charset="utf-8">
<title>Zottelgarten – Visitenkarte</title>
<link rel="stylesheet" href="https://fonts.googleapis.com/css2?family=Cinzel:wght@400;600;700&display=swap">
<style>
  :root {
    --backdrop: #0f7db6;
    --taupe: #7e6c5c;
    --paper: #ffffff;
    --ink: #222222;
    --mark-dark: #333333;
    --band-text: #f6f1ec;
  }
  html, body {
    margin: 0;
    padding: 0;
    width: 1200px;
    height: 1000px;
    overflow: hidden;
    background: var(--backdrop);
  }
  .canvas {
    position: relative;
    width: 1200px;
    height: 1000px;
    font-family: "Cinzel", "Trajan Pro", serif;
  }
  .card {
    position: absolute;
    top: 348px;
    width: 546px;
    height: 304px;
    overflow: hidden;
  }
  .card--front { left: 37px; background: var(--taupe); color: var(--paper); }
  .card--back { left: 617px; background: var(--paper); color: var(--ink); }

  .front-ring {
    position: absolute;
    left: 170px;
    top: 15px;
    width: 206px;
    height: 206px;
  }
  .front-name {
    position: absolute;
    left: 0;
    right: 0;
    top: 228px;
    margin: 0;
    text-align: center;
    font-weight: 400;
    font-size: 42px;
    letter-spacing: 3px;
    line-height: 1;
  }
  .front-url {
    position: absolute;
    left: 0;
    right: 0;
    top: 280px;
    text-align: center;
    font-size: 12px;
    letter-spacing: 6.5px;
    line-height: 1;
  }

  .back-dot {
    position: absolute;
    left: 232px;
    top: 22px;
    width: 84px;
    height: 84px;
  }
  .back-name {
    position: absolute;
    left: 0;
    right: 0;
    top: 118px;
    margin: 0;
    text-align: center;
    font-weight: 400;
    font-size: 20px;
    letter-spacing: 1.5px;
    line-height: 1;
  }
  .person-band {
    position: absolute;
    left: 0;
    right: 0;
    top: 163px;
    height: 60px;
    background: var(--taupe);
    color: var(--band-text);
    text-align: center;
  }
  .person-name {
    margin: 9px 0 0;
    font-weight: 700;
    font-size: 17px;
    letter-spacing: 0.5px;
    line-height: 1.1;
  }
  .person-title {
    margin: 2px 0 0;
    font-weight: 400;
    font-size: 16px;
    letter-spacing: 0.5px;
    line-height: 1.1;
  }
  .contact-row {
    position: absolute;
    left: 21px;
    right: 21px;
    top: 258px;
    display: flex;
    justify-content: space-between;
    font-size: 16px;
    letter-spacing: 0.3px;
    line-height: 1;
  }
</style>
</head>
<body>
<main class="canvas">
  <section class="card card--front" aria-label="Vorderseite">
    <svg class="front-ring" viewBox="0 0 206 206" aria-hidden="true">
      <circle cx="103" cy="103" r="101" fill="none" stroke="var(--paper)" stroke-width="3"/>
    </svg>
    <h1 class="front-name">ZOTTELGARTEN</h1>
    <div class="front-url">WWW.ZOTTELGARTEN.CH</div>
  </section>

  <section class="card card--back" aria-label="Rückseite">
    <svg class="back-dot" viewBox="0 0 84 84" aria-hidden="true">
      <circle cx="42" cy="42" r="42" fill="var(--mark-dark)"/>
    </svg>
    <h2 class="back-name">ZOTTELGARTEN</h2>
    <div class="person-band">
      <p class="person-name">Margit Wendler-Rasch</p>
      <p class="person-title">Dipl. Dog Trainer</p>
    </div>
    <div class="contact-row">
      <span class="contact-address">Lindenweg 12, Kemptthal</span>
      <span class="contact-phone">Tel: (123) 456-7890</span>
    </div>
  </section>
</main>
</body>
</html>
```